Cancer ppt courses for healthcare pro

We are organizing a contest for designers to modernize and improve an existing PowerPoint presentation titled "Along the Quiet Shore of Healing Days." This presentation is aimed at healthcare professionals, patients, and the general public, to inform them about the treatment and remission journey of breast cancer.
Objective
The goal of the contest is to create a visually appealing, clear, and professional PowerPoint presentation while maintaining the accuracy and precision of the medical information.
Requirements
Visual Design
Create a modern and consistent design for the entire presentation.
Use a soothing and professional color palette.
Integrate relevant visuals (icons, illustrations, photos) to support the content.
Ensure good readability with clear and appropriate fonts.
Structure and Organization
Maintain the logical and sequential structure of the existing content.
Reorganize information to improve clarity and flow if necessary.
Add smooth transitions between sections to facilitate understanding.
Thrilled
Preserve the integrity and accuracy of the medical information.
Highlight key points and important statistics.
Use charts and tables to present data visually and comprehensibly.
Updates
Faible participation designers
Target Market(s)
physiotherapist
Requirements
Must have
- it its new way of elarning courses, this presentation will be mixed with interviews, documentars... more like a movie

```html
<!DOCTYPE html>
<html lang="fr">
<head>
<meta charset="UTF-8">
<title>Anatomie du sein</title>
<link href="https://fonts.googleapis.com/css2?family=Inter:wght@400;700&family=Nunito:wght@800&display=swap" rel="stylesheet">
<style>
  :root {
    --bg: #fcedf3;
    --bg-soft: #f7dceb;
    --accent: #e2489b;
    --ink: #0d0d0d;
    --card: #ffffff;
    --illus-a: #f6c7d0;
    --illus-b: #f8d58f;
    --illus-c: #e98a78;
  }
  * { margin: 0; padding: 0; box-sizing: border-box; }
  html, body { width: 1200px; height: 675px; overflow: hidden; }
  body {
    position: relative;
    background:
      linear-gradient(115deg, transparent 30%, var(--bg-soft) 30%, var(--bg-soft) 42%, transparent 42%),
      linear-gradient(160deg, var(--bg) 0%, #fbe3ee 55%, var(--bg) 100%);
    font-family: "Inter", sans-serif;
    color: var(--ink);
  }
  .slide-frame {
    position: absolute;
    left: 23px; top: 26px;
    width: 1152px; height: 621px;
    border: 1.5px solid var(--accent);
    border-radius: 72px;
  }
  .slide-title {
    position: absolute;
    left: 100px; top: 2px;
    padding: 0 32px;
    background: var(--bg);
    color: var(--accent);
    font-weight: 400;
    font-size: 46px;
    line-height: 52px;
    letter-spacing: 0.3px;
  }
  .content {
    position: absolute;
    left: 138px; top: 206px;
  }
  .content-heading {
    font-size: 37px;
    font-weight: 700;
    line-height: 46px;
    margin-bottom: 6px;
  }
  .part-list { list-style: none; }
  .part-list li {
    position: relative;
    padding-left: 45px;
    font-size: 26px;
    line-height: 43.7px;
  }
  .part-list li.has-dot::before {
    content: "";
    position: absolute;
    left: 11px; top: 16px;
    width: 12px; height: 12px;
    border-radius: 50%;
    background: var(--accent);
  }
  .figure-card {
    position: absolute;
    left: 605px; top: 107px;
    width: 461px; height: 461px;
    background: var(--card);
    border-radius: 76px;
  }
  .figure-title {
    position: absolute;
    left: 0; right: 0; top: 46px;
    text-align: center;
    font-family: "Nunito", sans-serif;
    font-weight: 800;
    font-size: 12.5px;
    letter-spacing: 0.6px;
  }
  .figure-art {
    position: absolute;
    left: 61px; top: 89px;
    width: 332px; height: 319px;
    border-radius: 18px;
    background: radial-gradient(circle at 62% 58%, var(--illus-a) 0%, var(--illus-b) 45%, var(--illus-c) 80%, #f3d3d9 100%);
  }
</style>
</head>
<body>
  <div class="slide-frame"></div>
  <h1 class="slide-title">Anatomie du sein</h1>

  <section class="content">
    <h2 class="content-heading">La glande mammaire :</h2>
    <ul class="part-list">
      <li class="has-dot">Tissu graisseux</li>
      <li class="has-dot">Lobes</li>
      <li class="has-dot">Lobules</li>
      <li>Alvéoles</li>
      <li class="has-dot">Canaux galactophores</li>
    </ul>
  </section>

  <figure class="figure-card">
    <div class="figure-title">LE SEIN - ANATOMIE</div>
    <div class="figure-art" role="img" aria-label="Coupe anatomique du sein : clavicule, côtes, muscle grand pectoral, graisse, lobules, canaux, aréole et mamelon"></div>
  </figure>
</body>
</html>
```